Company Brochure / Sales Sheet

We would like a brochure that we will may print out as well as forward electronically to our prospective clients.

Our clients are inventors/doctors/surgeons of medical products who need help completing their medical product, gaining approval, and then selling their product into the US market

Target Market(s)

Inventors of medical products who want to sell them in the United States

Industry/Entity Type

Medical

Font styles to use
Serif
Sans Serif

Requirements
Must have
• The word "Medical" should not receive special empahsis.
• Use the last two photos and whatever other photos that look good. You can edit and crop the photos
• Text should be easy to read
Nice to have
• We want to show that we have a lot of products.
• Sharp, clean, modern
• Minimum two pages - final product should be capable of being printed and
• forwarded electronically
• Easy to read
Should not have
• Should not be cluttered

```html
<!DOCTYPE html>
<html lang="en">
<head>
<meta charset="utf-8">
<title>Veltrimed Partners – Company Brochure</title>
<link rel="stylesheet" href="https://fonts.googleapis.com/css2?family=Open+Sans:wght@400;600;700&display=swap">
<style>
  :root {
    --backdrop: #e4e4e6;
    --paper: #ffffff;
    --paper-shade: #f1f1f3;
    --purple: #6a3fa0;
    --purple-deep: #3f1f6e;
    --purple-light: #8a5cc4;
    --ink: #4a4a52;
    --black: #111114;
    --placeholder-a: #9bb6d6;
    --placeholder-b: #dfe6ef;
  }
  * { box-sizing: border-box; margin: 0; padding: 0; }
  html, body { width: 1200px; height: 863px; overflow: hidden; }
  body {
    background: var(--backdrop);
    font-family: "Open Sans", Arial, sans-serif;
    color: var(--ink);
    position: relative;
  }
  .spread {
    position: absolute; left: 80px; top: 62px;
    width: 1040px; height: 740px;
    display: flex;
    box-shadow: 0 14px 34px rgba(0,0,0,.22);
  }
  .page {
    position: relative; width: 520px; height: 740px;
    background: var(--paper);
    padding: 46px 44px 0;
    font-size: 10.5px; line-height: 1.6;
  }
  .page--left { background: linear-gradient(90deg, var(--paper) 85%, var(--paper-shade)); }
  .page--right { background: linear-gradient(90deg, var(--paper-shade), var(--paper) 15%); }
  .section-title {
    color: var(--purple); font-weight: 700; font-size: 14px;
    margin: 14px 0 6px;
  }
  .section-title--center { text-align: center; }
  .section-title--caps { text-transform: uppercase; font-size: 11.5px; letter-spacing: .04em; }
  p { margin-bottom: 8px; text-align: justify; }
  .expertise {
    display: grid; grid-template-columns: 1fr 1fr; gap: 4px 24px;
    list-style: none; margin: 8px 0 10px 20px;
  }
  .expertise li { display: flex; align-items: center; gap: 7px; font-size: 10px; color: var(--purple-deep); }
  .tick { width: 11px; height: 11px; flex: none; }
  .ip-block { display: flex; gap: 16px; align-items: flex-start; }
  .ip-block p { flex: 1; }
  .photo {
    background: linear-gradient(135deg, var(--placeholder-b), var(--placeholder-a));
    border: 1px solid #c9ced8;
  }
  .photo--device { width: 96px; height: 104px; flex: none; }
  .product-row { display: flex; justify-content: space-between; margin: 10px 0 12px; }
  .photo--product { width: 96px; height: 68px; }
  .photo--product.alt { background: linear-gradient(135deg, #2d4c86, #e4c23c); }
  .footer-band { position: absolute; left: 0; bottom: 0; width: 1040px; height: 230px; pointer-events: none; }
  .site-url {
    position: absolute; bottom: 34px; font-size: 8.5px; color: #e9defa;
    display: flex; align-items: center; gap: 6px; letter-spacing: .03em;
  }
  .site-url::before { content: ""; width: 9px; height: 9px; border-radius: 50%; background: #e9defa; }
  .site-url--left { left: 140px; bottom: 70px; }
  .site-url--right { left: 680px; bottom: 40px; }
</style>
</head>
<body>
<main class="spread">
  <section class="page page--left">
    <h2 class="section-title section-title--center">About Us</h2>
    <p>We are a network of medical product professionals, including physicians, engineers, regulatory and sales experts, who guide inventors from early concept through approval and launch. Our team brings decades of hands-on experience in device design, clinical testing and distribution across the United States.</p>
    <p>Our offices work closely with surgeons and doctors who have a promising idea but need a partner to finish the product, protect it and bring it to market. We share the risk, the planning and the results.</p>
    <p>From the first prototype to the first order, every step is handled by one dedicated team so that you can stay focused on patient care and new ideas.</p>

    <h2 class="section-title section-title--center">Our Expertise Include</h2>
    <ul class="expertise">
      <li><svg class="tick" viewBox="0 0 12 12"><path d="M1 6.5 4.5 10 11 2" fill="none" stroke="#6a3fa0" stroke-width="2"/></svg>Market Research</li>
      <li><svg class="tick" viewBox="0 0 12 12"><path d="M1 6.5 4.5 10 11 2" fill="none" stroke="#6a3fa0" stroke-width="2"/></svg>Manufacturing</li>
      <li><svg class="tick" viewBox="0 0 12 12"><path d="M1 6.5 4.5 10 11 2" fill="none" stroke="#6a3fa0" stroke-width="2"/></svg>Product Design</li>
      <li><svg class="tick" viewBox="0 0 12 12"><path d="M1 6.5 4.5 10 11 2" fill="none" stroke="#6a3fa0" stroke-width="2"/></svg>Distribution and Fulfilment</li>
      <li><svg class="tick" viewBox="0 0 12 12"><path d="M1 6.5 4.5 10 11 2" fill="none" stroke="#6a3fa0" stroke-width="2"/></svg>Clinical Study Support</li>
      <li><svg class="tick" viewBox="0 0 12 12"><path d="M1 6.5 4.5 10 11 2" fill="none" stroke="#6a3fa0" stroke-width="2"/></svg>Sales</li>
      <li><svg class="tick" viewBox="0 0 12 12"><path d="M1 6.5 4.5 10 11 2" fill="none" stroke="#6a3fa0" stroke-width="2"/></svg>Patent Protection</li>
      <li><svg class="tick" viewBox="0 0 12 12"><path d="M1 6.5 4.5 10 11 2" fill="none" stroke="#6a3fa0" stroke-width="2"/></svg>Branding and Marketing</li>
      <li><svg class="tick" viewBox="0 0 12 12"><path d="M1 6.5 4.5 10 11 2" fill="none" stroke="#6a3fa0" stroke-width="2"/></svg>Quality Systems and Compliance</li>
      <li><svg class="tick" viewBox="0 0 12 12"><path d="M1 6.5 4.5 10 11 2" fill="none" stroke="#6a3fa0" stroke-width="2"/></svg>Product Launch</li>
    </ul>

    <h2 class="section-title section-title--center">Medical Products</h2>
    <p>We specialise in the distribution of next generation medical products, including surgical instruments, monitoring and diagnostic devices, and advanced wound care.</p>
  </section>

  <section class="page page--right">
    <p>Our medical products represent breakthroughs in design and technology, serving clinics, hospitals and care centres nationwide.</p>

    <h2 class="section-title">Intellectual Property and Branding</h2>
    <div class="ip-block">
      <p>We help our partners file patents, register trademarks and build a brand that doctors trust. A clear name and identity make your product easier to sell and harder to imitate.</p>
      <div class="photo photo--device" role="img" aria-label="Photo of a blue portable medical monitoring device"></div>
    </div>

    <h2 class="section-title">Regulatory Issues</h2>
    <p>We prepare and manage FDA submissions, testing plans and labelling so your product meets every requirement before it reaches the market.</p>

    <h2 class="section-title section-title--caps">Latest Advanced Surgicals</h2>
    <p>Our experienced engineers refine each instrument for precision, comfort and safety, then support production and delivery to your customers.</p>
    <div class="product-row">
      <div class="photo photo--product" role="img" aria-label="Photo of steel surgical forceps"></div>
      <div class="photo photo--product alt" role="img" aria-label="Photo of a surgical instrument on a blue background"></div>
      <div class="photo photo--product" role="img" aria-label="Photo of a laparoscopic grasper tip"></div>
      <div class="photo photo--product" role="img" aria-label="Photo of a slim surgical probe"></div>
    </div>
    <p>We are especially focused on innovative products with rapid growth and clear market potential, and we partner with inventors to reach buyers quickly.</p>
    <p>We will help you when you need help the most, in launching your new products to market.</p>
  </section>

  <svg class="footer-band" viewBox="0 0 1040 230" preserveAspectRatio="none" aria-hidden="true">
    <defs>
      <linearGradient id="bandPurple" x1="0" y1="0" x2="0" y2="1">
        <stop offset="0" stop-color="#8a5cc4"/>
        <stop offset="1" stop-color="#4a2580"/>
      </linearGradient>
    </defs>
    <path d="M0,40 C160,140 360,190 520,150 C680,190 880,140 1040,40 L1040,230 L0,230 Z" fill="url(#bandPurple)"/>
    <path d="M0,40 C160,140 360,190 520,150 C680,190 880,140 1040,40" fill="none" stroke="#ffffff" stroke-width="3" opacity=".8"/>
    <path d="M0,130 L0,230 L110,230 Z" fill="#111114"/>
    <path d="M1040,130 L1040,230 L930,230 Z" fill="#111114"/>
    <path d="M455,230 L520,168 L585,230 Z" fill="#111114"/>
  </svg>
  <span class="site-url site-url--left">www.veltrimed.com</span>
  <span class="site-url site-url--right">www.veltrimed.com</span>
</main>
</body>
</html>
```